Pike Hauling Business Card Design Project

We need a new company business card. We provide professional timber harvesting (logging) and forest management services. I'm open to any creative design. Most company caps and shirts are navy blue and Light grey. Logo does not necessarily have to contain those colors. Logo containing picture of logging equipment, log truck, trees, or logs are acceptable. Be creative. Final logo should communicate our company's pride and professionalism in the East Texas Timber Industry.
Updates

Target Market(s)

Timber owners, sawmills, and forestry professionals

Industry/Entity Type

Business

Requirements
Must have
• Must have Contact Info.
Phone: 555-402-5187
address: PO Box 8412
Cedar Bend, Tx 75000
www.rbpikehauling.example
rbpikehauling@mailbox.example
Owner: Ross Pike

Or design must leave room for this info.

```html
<!DOCTYPE html>
<html lang="en">
<head>
<meta charset="utf-8">
<title>Pike Hauling Company – Business Card</title>
<link rel="stylesheet" href="https://fonts.googleapis.com/css2?family=Crimson+Text:wght@400;600&display=swap">
<style>
  :root {
    --backdrop: #e9e4dc;
    --card-dark: #2a150c;
    --card-dark-panel: #3a2116;
    --card-light: #ffffff;
    --ink: #2b1a12;
    --ink-on-dark: #f4efe8;
    --wood-light: #f2c98a;
    --wood-mid: #dc9a4c;
    --wood-deep: #a9622a;
  }
  * { box-sizing: border-box; margin: 0; padding: 0; }
  html, body { width: 1200px; height: 900px; overflow: hidden; }
  body {
    background: var(--backdrop);
    font-family: "Crimson Text", Georgia, serif;
    color: var(--ink);
    position: relative;
  }
  .card {
    position: absolute;
    width: 640px;
    height: 366px;
    box-shadow: 0 10px 28px rgba(0,0,0,.22);
  }

  /* Back of card */
  .card-back {
    left: 180px; top: 60px;
    background: radial-gradient(ellipse at 40% 45%, #3b2015 0%, var(--card-dark) 70%);
  }
  .card-back .brand-panel {
    position: absolute;
    left: 70px; top: 110px;
    width: 420px; height: 140px;
    background: var(--card-dark-panel);
    display: flex; align-items: center; justify-content: center;
  }
  .card-back .brand { color: var(--ink-on-dark); }

  .brand {
    display: flex; align-items: center; gap: 18px;
    font-weight: 400;
    letter-spacing: 1.5px;
    text-transform: uppercase;
  }
  .brand-initials { font-size: 64px; line-height: 1; }
  .brand-words { font-size: 22px; line-height: 1.05; }

  /* Front of card */
  .card-front {
    left: 380px; top: 470px;
    background: var(--card-light);
    overflow: hidden;
  }
  .card-front .brand {
    position: absolute;
    left: 40px; top: 74px;
    color: var(--ink);
  }
  .owner {
    position: absolute;
    right: 170px; top: 26px;
    text-align: right;
  }
  .owner-name { font-size: 22px; font-weight: 600; letter-spacing: .5px; text-transform: uppercase; }
  .owner-title { font-size: 14px; }

  .contact {
    position: absolute;
    left: 40px; bottom: 26px;
    list-style: none;
    font-size: 19px;
    line-height: 1.3;
  }
  .contact li { display: flex; align-items: center; gap: 10px; }
  .contact svg { width: 15px; height: 15px; fill: var(--ink); flex: none; }

  .log-stack {
    position: absolute;
    right: 0; top: 110px;
    width: 160px; height: 256px;
    border-radius: 90px 0 0 20px;
    background: radial-gradient(circle at 45% 40%, var(--wood-light) 0%, var(--wood-mid) 55%, var(--wood-deep) 100%);
  }
</style>
</head>
<body>
  <section class="card card-back">
    <div class="brand-panel">
      <div class="brand">
        <span class="brand-initials">RB</span>
        <span class="brand-words">Pike<br>Hauling<br>Company</span>
      </div>
    </div>
  </section>

  <section class="card card-front">
    <div class="owner">
      <p class="owner-name">Ross Pike</p>
      <p class="owner-title">Owner</p>
    </div>

    <div class="brand">
      <span class="brand-initials">RB</span>
      <span class="brand-words">Pike<br>Hauling<br>Company</span>
    </div>

    <ul class="contact">
      <li>
        <svg viewBox="0 0 16 16" aria-hidden="true"><path d="M3.5 1.5l2.5 3-1.5 1.5c.8 2 2.5 3.7 4.5 4.5L10.5 9l3 2.5-1.5 2.5C7 14 2 9 2 3z"/></svg>
        555-402-5187
      </li>
      <li>
        <svg viewBox="0 0 16 16" aria-hidden="true"><circle cx="3" cy="13" r="2"/><path d="M1 7a8 8 0 0 1 8 8H7a6 6 0 0 0-6-6zM1 2a13 13 0 0 1 13 13h-2A11 11 0 0 0 1 4z"/></svg>
        www.rbpikehauling.example
      </li>
      <li>
        <svg viewBox="0 0 16 16" aria-hidden="true"><path d="M1 4h14v9H1zm1.5 1.2v.4L8 9.5l5.5-3.9v-.4z"/></svg>
        rbpikehauling@mailbox.example
      </li>
      <li>
        <svg viewBox="0 0 16 16" aria-hidden="true"><path d="M8 1a4.5 4.5 0 0 1 4.5 4.5C12.5 9 8 13 8 13S3.5 9 3.5 5.5A4.5 4.5 0 0 1 8 1zm0 2.5a2 2 0 1 0 0 4 2 2 0 0 0 0-4zM2 14h12v1.5H2z"/></svg>
        PO Box 8412, Cedar Bend, Tx 75000
      </li>
    </ul>

    <div class="log-stack" role="img" aria-label="Illustration of stacked cut log ends showing tree rings"></div>
  </section>
</body>
</html>
```